Bright Pathways Benefit Golf Classic

we are looking for help designing a trifold brochure that could accompany the attached letter, both being mailed in a #10 envelope. With the amount of sponsorship copy, it be a good idea to put the detailed sponsorship level content on a single one-page flyer. One section of the trifold could be a summary level of the sponsorship level and allow the sponsor tear-off that part and mail in their payment. I want the color scheme and design to align with our website https://brightpathwayscare.org while not losing sight that this is a charity golf tournament. The sponsorship detail is not finalized but is directionally correct as shown on page 2 of the letter. What might be ideal is to have a tri-fold, a bi-fold which would contain details of the event along with the copy on the letter, while the one-page flyer would have the detailed sponsor levels & details.

I would also be open to alternative ideas if you think there's a better way of doing this. For example, could we put everything into a one 2-page brochure that would be the same size as the letter. There could be a tear out to mail back but this could fit into an envelope that could accommodate an unfolded 8.5x11 letter. I think this could work but will let you think about best options.

Target Market(s)

Corporate sponsors and serious golfers

Industry/Entity Type

Non-Profit

Font styles to use
Serif

Requirements
Must have
• Event Date: August 23, 2021
Event Location: Maple Ridge County Club, 47 Larkfield Road, Ashford Falls
Schedule:
Lunch: 11:00
Shotgun Start: 12:30
Open Bar Reception: 5:00
Dinner: 6:00

At the moment, the sponsorship levels, pricing, and inclusions are directionally correct.

BPC Brand Colors:
#08143A
#FFCD35
#980909
#11808B
#3C2C83

Ok to use any images from the Maple Ridge CC website.
Nice to have
• We have a lot of copy & content to share, so I am not locked into a trifold - bifold concept if a single full size 2-sheet (8 pages) would work better as long as there would be a way for the sponsor to 'tear off' the summary order form. If you think the full size version is a better single option to go with our letter, I would like to use some images from our website along to give the event the seriousness it deserves while still being a golf tournament. This will be our first annual tournament although I am not sure that's important to include.
Should not have
• emojis, clip art.

```html
<!DOCTYPE html>
<html lang="en">
<head>
<meta charset="utf-8">
<title>Bright Pathways Benefit Golf Classic – Sponsorship Brochure</title>
<link href="https://fonts.googleapis.com/css2?family=Cinzel:wght@500;700&family=Lora:ital,wght@0,400;0,600;0,700;1,400;1,600&display=swap" rel="stylesheet">
<style>
  :root{
    --navy:#08143A;
    --gold:#FFCD35;
    --gold-deep:#f0b91d;
    --paper:#ffffff;
    --ink:#2b2f3a;
    --muted:#6b6f7a;
    --rule:#d9dbe2;
    --stage:#e4e4e2;
    --display:"Cinzel", "Times New Roman", serif;
    --text:"Lora", Georgia, serif;
  }
  *{box-sizing:border-box;margin:0;padding:0}
  html,body{width:1200px;height:2400px;overflow:hidden;background:var(--stage)}
  .canvas{position:relative;width:1200px;height:2400px;overflow:hidden;background:var(--stage);font-family:var(--text);color:var(--ink)}

  .sheet{position:absolute;left:42px;width:1116px;height:1080px;display:flex;box-shadow:0 6px 22px rgba(0,0,0,.18)}
  .sheet--outside{top:60px}
  .sheet--inside{top:1240px}
  .panel{position:relative;width:372px;height:100%;overflow:hidden}
  .panel + .panel{border-left:1px solid rgba(0,0,0,.08)}
  .panel--paper{background:var(--paper)}
  .panel--navy{background:var(--navy);color:#fff}
  .panel--wide{width:744px}

  .photo{position:absolute;left:0;width:100%}
  .curve{position:absolute;left:0;width:100%;display:block}

  .wordmark{display:flex;flex-direction:column;align-items:center;font-family:var(--display);color:var(--navy)}
  .wordmark__initials{font-size:54px;font-weight:700;letter-spacing:6px;line-height:1}
  .wordmark__name{font-size:17px;font-weight:700;letter-spacing:2px;margin-top:6px;text-transform:uppercase}
  .wordmark--light{color:#fff}

  .flap__photo{top:0;height:330px;background:linear-gradient(135deg,#6a7f62 0%,#c9b79a 40%,#8a8d7c 70%,#3c4a3a 100%)}
  .flap__curve{top:280px}
  .badge{position:absolute;left:26px;top:300px;width:96px;height:96px;border-radius:50%;background:#fff;border:3px solid var(--navy)}
  .flap__body{position:absolute;left:28px;right:28px;top:410px}
  .section-title{font-family:var(--display);font-weight:700;color:var(--navy);font-size:22px;letter-spacing:1px;line-height:1.2}
  .body-copy{font-size:13px;line-height:1.65;color:var(--ink);margin-top:14px}
  .partners{margin-top:22px}
  .partners__title{font-family:var(--text);font-weight:700;color:var(--navy);font-size:19px;text-align:right}
  .partners__row{display:flex;gap:14px;margin-top:14px}
  .partner-mark{width:100px;height:44px;background:#e9ecf3;border-radius:4px}
  .partner-mark--round{width:44px;border-radius:50%}
  .flap__footer{position:absolute;left:0;right:0;bottom:0;height:62px;background:var(--gold);display:flex;align-items:center;padding-left:28px;font-size:14px;font-weight:600;color:var(--navy);border-top-right-radius:40px}

  .back{padding:44px 30px 0;text-align:center}
  .back .wordmark{margin-bottom:28px}
  .invite{font-style:italic;font-weight:600;color:var(--gold);font-size:17px;line-height:1.45}
  .back .body-copy{color:#e6e9f2;text-align:left;font-size:12.5px}
  .signoff{font-style:italic;color:#e6e9f2;font-size:12.5px;margin-top:12px;text-align:left}
  .details{margin-top:30px;line-height:1.5}
  .details dt{font-family:var(--display);font-size:15px;color:var(--gold);letter-spacing:1px;margin-top:12px}
  .details dd{font-size:15px;color:#fff}
  .schedule{list-style:none;margin-top:6px;font-family:var(--display);font-size:15px;letter-spacing:.5px;line-height:1.75}
  .contact{position:absolute;left:0;right:0;bottom:0;height:200px;background:var(--gold);border-top-left-radius:44px;padding:22px 30px;color:var(--navy);text-align:left}
  .contact__title{font-weight:700;font-size:13px;letter-spacing:1px;text-transform:uppercase;text-align:center;margin-bottom:16px}
  .contact__line{display:flex;align-items:center;gap:12px;font-size:14px;font-weight:600;margin-top:10px}
  .contact__line svg{flex:none}

  .cover__head{position:absolute;top:0;left:0;right:0;height:260px;padding-top:70px}
  .cover__curve{top:190px}
  .cover__photo{top:250px;height:500px;background:linear-gradient(180deg,#b9a46a 0%,#7d8d4a 35%,#4f7a2f 65%,#2f5a1d 100%)}
  .cover__band{position:absolute;left:0;right:0;bottom:0;height:340px;background:var(--navy);padding:76px 24px 0;text-align:center}
  .cover__band-curve{top:720px}
  .cover__title{font-family:var(--display);font-weight:700;color:var(--gold);font-size:23px;letter-spacing:1px;line-height:1.2;white-space:nowrap}
  .cover__rule{height:2px;background:var(--gold);margin:18px 10px}
  .cover__subtitle{font-family:var(--text);color:#fff;font-size:24px;line-height:1.3}
  .date-pill{display:inline-block;margin-top:26px;background:var(--gold);color:var(--navy);font-family:var(--display);font-weight:700;font-size:20px;letter-spacing:2px;padding:12px 40px;border-radius:26px}

  .intro{padding:48px 30px 0}
  .intro__title{font-family:var(--text);font-weight:700;color:var(--gold);font-size:25px;line-height:1.25}
  .intro .body-copy{color:#e6e9f2;font-size:12.5px}
  .callout{margin-top:18px;background:var(--gold);color:var(--navy);font-weight:700;font-size:13.5px;line-height:1.5;padding:12px 16px;text-align:center}
  .intro__photo{bottom:0;height:260px;background:linear-gradient(180deg,#8fb3d6 0%,#a7c08b 45%,#4f7d34 100%)}
  .intro__curve{bottom:230px}

  .levels__photo{top:0;height:250px;background:linear-gradient(135deg,#c9cfd6 0%,#e8e6df 40%,#7a8a6a 75%,#4e6b3d 100%)}
  .levels__curve{top:206px}
  .levels__badge{position:absolute;right:36px;top:26px;width:110px;height:110px;border-radius:50%;background:#fff;border:3px solid var(--navy)}
  .levels__body{position:absolute;left:36px;right:36px;top:270px}
  .levels__title{font-family:var(--text);font-weight:700;color:var(--navy);font-size:26px;text-align:center}
  .levels__note{font-size:12px;color:var(--muted);text-align:center;margin-top:4px}
  .levels__table{width:100%;border-collapse:collapse;margin-top:18px}
  .levels__table td{border-bottom:1px solid var(--rule);padding:9px 6px;vertical-align:middle}
  .tick-box{width:20px;height:20px;border:2px solid var(--gold-deep);display:block}
  .level-name{font-weight:700;color:var(--navy);font-size:14px;width:190px}
  .level-perks{font-size:11.5px;color:var(--muted);line-height:1.4}
  .level-price{font-weight:700;color:var(--navy);font-size:15px;text-align:right;width:80px}
  .order-form{margin-top:22px;display:grid;grid-template-columns:1fr 1fr;gap:12px 28px}
  .field{font-size:12px;color:var(--navy);font-weight:600;border-bottom:1px solid var(--navy);padding-bottom:12px}
  .order-form__note{grid-column:1 / -1;font-size:11.5px;color:var(--muted);font-style:italic}
</style>
</head>
<body>
<main class="canvas">

  <section class="sheet sheet--outside" aria-label="Brochure outside">

    <article class="panel panel--paper flap">
      <div class="photo flap__photo" role="img" aria-label="Photo of a smiling resident with family members"></div>
      <svg class="curve flap__curve" viewBox="0 0 372 80" height="80" preserveAspectRatio="none" aria-hidden="true">
        <path d="M0 44 Q186 -6 372 30 L372 80 L0 80 Z" fill="#fff"/>
        <path d="M0 44 Q186 -6 372 30" stroke="var(--gold)" stroke-width="5" fill="none"/>
      </svg>
      <div class="badge" aria-hidden="true"></div>
      <div class="flap__body">
        <h2 class="section-title">BENEFIT GOLF CLASSIC</h2>
        <p class="body-copy">Bright Pathways Care is hosting its first benefit golf classic to raise funds for adults with intellectual and developmental disabilities. Every dollar raised supports safe, supported homes and lasting community inclusion across Cedar and Harlow County.</p>
        <p class="body-copy">Join local businesses and golfers for a day on the course that helps our residents live full and independent lives.</p>
        <p class="body-copy">Sponsors receive recognition at the event, on our website and in printed materials shared with guests and supporters.</p>
        <div class="partners">
          <h3 class="partners__title">Our Partners.</h3>
          <div class="partners__row">
            <span class="partner-mark"></span>
            <span class="partner-mark partner-mark--round"></span>
            <span class="partner-mark"></span>
          </div>
        </div>
      </div>
      <div class="flap__footer">www.brightpathwayscare.org</div>
    </article>

    <article class="panel panel--navy back">
      <div class="wordmark wordmark--light">
        <span class="wordmark__initials">BPC</span>
        <span class="wordmark__name">Bright Pathways Care</span>
      </div>
      <p class="invite">Please join Bright Pathways Care in sponsoring the 2021 Rising Stars Benefit Golf Classic.</p>
      <p class="body-copy">We have many different sponsorship levels available to you. Your support will help us provide safe and supportive homes for adults with disabilities.</p>
      <p class="body-copy">In order to secure your logo, signs and banners, please return the sponsorship form by July 15th.</p>
      <p class="signoff">Thank you for your consideration!<br>Rising Stars Committee Chair</p>
      <dl class="details">
        <dt>EVENT DATE:</dt>
        <dd>August 23, 2021</dd>
        <dt>EVENT LOCATION:</dt>
        <dd>Maple Ridge County Club, 47 Larkfield Road<br>Ashford Falls</dd>
        <dt>SCHEDULE:</dt>
      </dl>
      <ul class="schedule">
        <li>LUNCH: 11:00</li>
        <li>SHOTGUN START: 12:30</li>
        <li>OPEN BAR RECEPTION: 5:00</li>
        <li>DINNER: 6:00</li>
      </ul>
      <div class="contact">
        <p class="contact__title">For more information please contact us</p>
        <p class="contact__line">
          <svg width="22" height="22" viewBox="0 0 24 24" aria-hidden="true"><circle cx="12" cy="12" r="12" fill="var(--navy)"/><path d="M8.5 6.5l2 2-1.2 1.6c.8 1.6 2 2.8 3.6 3.6l1.6-1.2 2 2-1.4 1.6c-3.8-.4-7.8-4.4-8.2-8.2z" fill="#fff"/></svg>
          (555) 014-2290
        </p>
        <p class="contact__line">
          <svg width="22" height="22" viewBox="0 0 24 24" aria-hidden="true"><circle cx="12" cy="12" r="12" fill="var(--navy)"/><rect x="6" y="8" width="12" height="8" fill="none" stroke="#fff" stroke-width="1.5"/><path d="M6 8l6 5 6-5" fill="none" stroke="#fff" stroke-width="1.5"/></svg>
          info@brightpathwayscare.org
        </p>
        <p class="contact__line">
          <svg width="22" height="22" viewBox="0 0 24 24" aria-hidden="true"><circle cx="12" cy="12" r="12" fill="var(--navy)"/><circle cx="12" cy="12" r="6" fill="none" stroke="#fff" stroke-width="1.4"/><path d="M6 12h12M12 6c-2.4 3.6-2.4 8.4 0 12M12 6c2.4 3.6 2.4 8.4 0 12" fill="none" stroke="#fff" stroke-width="1.2"/></svg>
          www.brightpathwayscare.org
        </p>
      </div>
    </article>

    <article class="panel panel--paper cover">
      <div class="photo cover__photo" role="img" aria-label="Close-up photo of a golf ball on a tee beside a driver on the fairway"></div>
      <div class="cover__head panel--paper">
        <div class="wordmark">
          <span class="wordmark__initials">BPC</span>
          <span class="wordmark__name">Bright Pathways Care</span>
        </div>
      </div>
      <svg class="curve cover__curve" viewBox="0 0 372 90" height="90" preserveAspectRatio="none" aria-hidden="true">
        <path d="M0 0 L372 0 L372 30 Q186 80 0 54 Z" fill="#fff"/>
        <path d="M0 54 Q186 80 372 30" stroke="var(--gold)" stroke-width="5" fill="none"/>
      </svg>
      <div class="cover__band">
        <h1 class="cover__title">BENEFIT GOLF CLASSIC</h1>
        <div class="cover__rule"></div>
        <p class="cover__subtitle">2021 Hybrid Golf Event<br>Sponsorship Proposal</p>
        <span class="date-pill">AUGUST 23, 2021</span>
      </div>
      <svg class="curve cover__band-curve" viewBox="0 0 372 60" height="60" preserveAspectRatio="none" aria-hidden="true">
        <path d="M0 40 Q186 0 372 14 L372 60 L0 60 Z" fill="var(--navy)"/>
        <path d="M0 52 Q186 12 372 26" stroke="var(--gold)" stroke-width="3" fill="none"/>
      </svg>
    </article>
  </section>

  <section class="sheet sheet--inside" aria-label="Brochure inside">

    <article class="panel panel--navy intro">
      <h2 class="intro__title">2021 Hybrid Golf Event Sponsorship Proposal</h2>
      <p class="body-copy">The Bright Pathways Care Rising Stars Committee is planning a benefit golf tournament to raise funds for adults with intellectual and developmental disabilities in Cedar and Harlow County.</p>
      <p class="callout">The tournament will be held on Monday, August 23, at the Maple Ridge County Club in Ashford Falls.</p>
      <p class="body-copy">Our mission is to offer adult residences and support services so that every person can live as independently as possible in a caring home within their own community.</p>
      <p class="body-copy">We are actively supporting the unique and evolving needs of adults whose care needs are higher than standard group homes can provide.</p>
      <p class="body-copy">The alternative can be heartbreaking. Instead, we provide homes that encourage growth, friendships, employment and full participation in the wider community.</p>
      <svg class="curve intro__curve" viewBox="0 0 372 60" height="60" preserveAspectRatio="none" aria-hidden="true">
        <path d="M0 60 L0 30 Q186 -4 372 24 L372 60 Z" fill="var(--gold)"/>
      </svg>
      <div class="photo intro__photo" role="img" aria-label="Photo of a golfer following through on a swing above a green valley"></div>
    </article>

    <article class="panel panel--paper panel--wide levels">
      <div class="photo levels__photo" role="img" aria-label="Photo of the country club entrance with guests on the porch"></div>
      <div class="levels__badge" aria-hidden="true"></div>
      <svg class="curve levels__curve" viewBox="0 0 744 70" height="70" preserveAspectRatio="none" aria-hidden="true">
        <path d="M0 50 Q372 0 744 36 L744 70 L0 70 Z" fill="#fff"/>
        <path d="M0 50 Q372 0 744 36" stroke="var(--gold)" stroke-width="5" fill="none"/>
      </svg>
      <div class="levels__body">
        <h2 class="levels__title">2021 Hybrid Golf Event Sponsorship Opportunities</h2>
        <p class="levels__note">Check the level you choose and return this form with your payment.</p>
        <table class="levels__table">
          <tr><td><span class="tick-box"></span></td><td class="level-name">Presenting Sponsor</td><td class="level-perks">Name on all event materials, two foursomes and dinner.</td><td class="level-price">$7,500</td></tr>
          <tr><td><span class="tick-box"></span></td><td class="level-name">Promotion Co-Sponsor</td><td class="level-perks">Logo on banners and website, one foursome included.</td><td class="level-price">$5,000</td></tr>
          <tr><td><span class="tick-box"></span></td><td class="level-name">Technology Sponsor</td><td class="level-perks">Recognition on scoring screens and online event pages.</td><td class="level-price">$3,000</td></tr>
          <tr><td><span class="tick-box"></span></td><td class="level-name">Corporate Sponsor with Golf Foursome</td><td class="level-perks">One foursome, hole sign and dinner recognition.</td><td class="level-price">$2,500</td></tr>
          <tr><td><span class="tick-box"></span></td><td class="level-name">Pin Flag Sponsor</td><td class="level-perks">Your name printed on every pin flag on course.</td><td class="level-price">$2,000</td></tr>
          <tr><td><span class="tick-box"></span></td><td class="level-name">Golf Cart Sponsor</td><td class="level-perks">Name displayed on all golf carts during play.</td><td class="level-price">$1,500</td></tr>
          <tr><td><span class="tick-box"></span></td><td class="level-name">Corporate Sponsor without Golf Foursome</td><td class="level-perks">Listing in program and thanks at the dinner.</td><td class="level-price">$1,000</td></tr>
          <tr><td><span class="tick-box"></span></td><td class="level-name">Flight Sponsor</td><td class="level-perks">Recognition on one flight of the scoreboard.</td><td class="level-price">$500</td></tr>
          <tr><td><span class="tick-box"></span></td><td class="level-name">Hole Sponsor</td><td class="level-perks">Sign with your name placed at one tee box.</td><td class="level-price">$250</td></tr>
        </table>
        <div class="order-form">
          <span class="field">Company Name</span>
          <span class="field">Contact Name</span>
          <span class="field">Phone</span>
          <span class="field">Email</span>
          <p class="order-form__note">Please make checks payable to Bright Pathways Care and mail by July 15, 2021.</p>
        </div>
      </div>
    </article>
  </section>

</main>
</body>
</html>
```